Business Card Design

Marla Quenby
Artist of Contemporary/Modern/Representational Art
Contact: 0429175348
Please include my web site (thanks)! http://www.artloft583.com.au/marla-quenby
And
Email: marlaquenby@vexmail.com

Target Market(s)

Modern professional People who know what they like in modern contemporary art and have the means to purchase it.

Industry/Entity Type

Business

Contact Information for Business Card

Marla Quenby
Contact: 0429175348

Font styles to use
Sans Serif

Requirements
Must have
• Simplicity & to the point
Keep the font modern/ contemporary
Nice to have
• A portrait of me and one piece of work on the business card (one on each side).
Should not have
• I'm not into butterflies.
No feminine style swirls
Nor I like swirls that look like tatoos

```html
<!DOCTYPE html>
<html lang="en">
<head>
<meta charset="utf-8">
<title>Marla Quenby — Business Card</title>
<link rel="stylesheet" href="https://fonts.googleapis.com/css2?family=Righteous&family=Alegreya:wght@700&display=swap">
<style>
  :root {
    --page: #ffffff;
    --name-panel: #f7f7f9;
    --ink: #111111;
    --band: #000000;
    --band-text: #ffffff;
    --sky-deep: #1f3f6e;
    --sky: #3f86b8;
    --roof: #8fa85a;
    --facade-red: #c8322c;
    --facade-yellow: #e7cf3a;
    --facade-green: #7d9d57;
    --street: #6b4a3a;
    --blossom: #b58a86;
  }
  html, body {
    margin: 0;
    padding: 0;
    width: 1200px;
    height: 1200px;
    overflow: hidden;
    background: var(--page);
  }
  .card {
    position: relative;
    width: 1200px;
    height: 1200px;
    background: var(--page);
  }
  .name-panel {
    position: absolute;
    left: 86px;
    top: 50px;
    width: 994px;
    height: 286px;
    background: var(--name-panel);
  }
  .artist-name {
    position: absolute;
    left: 0;
    right: 0;
    top: 248px;
    margin: 0;
    text-align: center;
    font-family: "Righteous", sans-serif;
    font-size: 68px;
    line-height: 1;
    color: var(--ink);
    letter-spacing: 1px;
    padding-right: 6px;
  }
  .info-band {
    position: absolute;
    left: 134px;
    top: 336px;
    width: 908px;
    height: 260px;
    background: var(--band);
    color: var(--band-text);
    font-family: "Alegreya", serif;
    font-weight: 700;
  }
  .tagline {
    position: absolute;
    left: 0;
    right: 0;
    top: 10px;
    margin: 0;
    text-align: center;
    font-size: 20.5px;
    padding-right: 38px;
  }
  .contact {
    position: absolute;
    right: 56px;
    top: 126px;
    margin: 0;
    text-align: right;
    font-size: 22px;
    line-height: 32px;
  }
  .artwork {
    position: absolute;
    left: 126px;
    top: 628px;
    width: 912px;
    height: 542px;
    background:
      linear-gradient(180deg,
        var(--sky-deep) 0%,
        var(--sky) 14%,
        var(--roof) 22%,
        var(--facade-red) 38%,
        var(--facade-yellow) 52%,
        var(--facade-green) 64%,
        var(--street) 80%,
        var(--blossom) 100%);
  }
</style>
</head>
<body>
  <main class="card">
    <div class="name-panel"></div>
    <h1 class="artist-name">Marla Quenby</h1>

    <section class="info-band">
      <p class="tagline">Artist of Contemporary/Modern/Representational Art</p>
      <p class="contact">
        Contact: 0429175348<br>
        www.artloft583.com.au/marla-quenby
      </p>
    </section>

    <div class="artwork" role="img"
         aria-label="Painting of a row of colourful, leaning European town houses in red, green, yellow and ochre under a deep blue sky, with a reflective street and blossoming trees in the foreground"></div>
  </main>
</body>
</html>
```